Professionelles Webdesign für hochwertiges Coaching Business
Zielgruppe
Es geht um eine Coaching-Firma für Einzelcoaching, Team-Coaching in Firmen und Ausbildungen. Inhalt sind Kommunikation, Stressmanagement und Leistungssteigerung, Persönlichkeitsentwicklung bis hin zum Marketing für Coaches.
Aufgabenstellung
- siehe Briefing im Dateiupload
- Umsetzung via Baukastensystem. Wichtig ist, dass die Features mit dem Baukastensystem umsetzbar sind.
- Es dürfen bitte diese 4 Seiten gestaltet werden:
Startseite
Coaching
Training
Ausbildung
- Obgleich ich Kundenfokus auf der Website bevorzuge, darf sie mich auch etwas widerspiegeln. Für einen Eindruck über mich sind zwei Bilder dem Anhang beigefügt. Diese Bilder sollen NICHT in die Website eingebunden werden.

```html
<!DOCTYPE html>
<html lang="de">
<head>
<meta charset="utf-8">
<title>Holmberg Training &amp; Coaching – Editor</title>
<link href="https://fonts.googleapis.com/css2?family=Abel&family=Inter:wght@400;500;600&family=IBM+Plex+Mono:wght@300;400&display=swap" rel="stylesheet">
<style>
:root{
  --panel:#f6f6f6;
  --ink:#1a1a1a;
  --muted:#666;
  --white:#ffffff;
  --brand-red:#9b1c24;
  --band-blue:#4b9aba;
  --notice:#3e3e3e;
  --navy:#1c3a6a;
  --photo-a:#b9a393;
  --photo-b:#7a5640;
  --photo-c:#3c2a22;
}
*{box-sizing:border-box;margin:0;padding:0}
html,body{width:1200px;height:778px;overflow:hidden;background:var(--panel);font-family:"Inter",sans-serif;color:var(--ink)}
.app{position:relative;width:1200px;height:778px}
.sidebar{position:absolute;left:0;top:0;width:221px;height:749px}
.app-mark{position:absolute;left:21px;top:20px;font-size:11px;font-weight:600;letter-spacing:.02em}
.search-icon{position:absolute;left:193px;top:20px}
.main-nav{position:absolute;left:21px;top:101px;list-style:none}
.main-nav li{font-size:14.5px;font-weight:500;height:26px;line-height:18px}
.main-nav li.active span{border-bottom:1.5px solid var(--ink);padding-bottom:1px}
.user{position:absolute;left:21px;top:703px;display:flex;align-items:center}
.avatar{width:29px;height:29px;border-radius:50%;background:#5a4a42}
.user-text{margin-left:10px;font-size:8px;line-height:11px}
.user-text .email{color:var(--muted)}
.badge{position:absolute;left:186px;top:711px;width:14px;height:14px;border-radius:50%;background:var(--ink);color:#fff;font-size:7px;display:flex;align-items:center;justify-content:center}
.frame{position:absolute;left:221px;top:9px;width:967px;height:740px;background:var(--white);overflow:hidden}
.topbar{height:36px;border-bottom:1px solid #ececec;position:relative}
.edit-label{position:absolute;left:15px;top:13px;font-size:8px;font-weight:600;letter-spacing:.04em}
.page-info{position:absolute;left:0;right:0;top:7px;text-align:center;font-size:7.5px;line-height:10px}
.page-info .state{color:var(--muted);font-weight:500}
.device-toggle{position:absolute;right:38px;top:7px;display:flex;background:#f0f0f0;border-radius:3px}
.device-toggle span{width:30px;height:22px;display:flex;align-items:center;justify-content:center}
.device-toggle span.on{background:#fff}
.open-icon{position:absolute;right:14px;top:11px}
.site-header{height:84px;position:relative}
.site-logo{position:absolute;left:44px;top:30px;display:flex;align-items:center;font-family:"IBM Plex Mono",monospace}
.site-logo .dot{width:10px;height:10px;border-radius:50%;background:var(--brand-red);margin-right:8px}
.site-logo .name{font-size:15px;color:var(--brand-red);letter-spacing:.06em;font-weight:400}
.site-nav{position:absolute;left:509px;top:34px;display:flex;align-items:center;font-family:"IBM Plex Mono",monospace;font-weight:300;font-size:11px;letter-spacing:.02em}
.site-nav a{color:var(--ink);text-decoration:none;margin-right:17px}
.site-nav .profile{width:9px;height:9px;background:var(--ink);margin:0 21px 0 2px}
.hero{position:absolute;top:120px;left:0;width:967px;height:466px;background:linear-gradient(100deg,var(--photo-a) 0%,#9c8170 35%,var(--photo-b) 60%,var(--photo-c) 100%)}
.hero-links{position:absolute;left:193px;top:90px;list-style:none;font-family:"Abel",sans-serif}
.hero-links li{font-size:42px;line-height:72px;height:72px}
.hero-links a{color:#fff;text-decoration:none;border-bottom:1px solid #fff;padding-bottom:0}
.intro{position:absolute;top:586px;left:0;width:967px;height:97px;background:var(--band-blue);text-align:center;font-family:"Abel",sans-serif;color:#fff;font-size:22px;padding-top:60px;overflow:hidden}
.notice{position:absolute;top:683px;left:0;width:967px;height:57px;background:var(--notice);color:#fff;font-size:7.6px;font-weight:500;letter-spacing:.03em;text-align:center;line-height:57px}
.help{position:absolute;left:909px;top:658px;width:36px;height:36px;border-radius:50%;background:#111;color:#fff;font-size:13px;display:flex;align-items:center;justify-content:center}
.trial{position:absolute;left:221px;top:749px;width:979px;height:29px;font-size:9.5px;display:flex;align-items:center;justify-content:center;gap:10px;padding-top:6px}
.trial .cta{background:var(--navy);color:#fff;font-size:8px;font-weight:600;letter-spacing:.05em;padding:5px 7px}
</style>
</head>
<body>
<div class="app">
  <aside class="sidebar">
    <div class="app-mark">Seitwerk</div>
    <svg class="search-icon" width="13" height="13" viewBox="0 0 13 13"><circle cx="5.5" cy="5.5" r="4.3" fill="none" stroke="#1a1a1a" stroke-width="1.4"/><line x1="8.6" y1="8.6" x2="12" y2="12" stroke="#1a1a1a" stroke-width="1.4"/></svg>
    <ul class="main-nav">
      <li>Seiten</li>
      <li>Design</li>
      <li class="active"><span>E-Commerce</span></li>
      <li>Marketing</li>
      <li>Scheduling</li>
      <li>Inhaltsbibliothek</li>
      <li>Analytics</li>
      <li>Profile</li>
      <li>Einstellungen</li>
      <li>Hilfe</li>
    </ul>
    <div class="user">
      <div class="avatar" role="img" aria-label="Profilbild"></div>
      <div class="user-text"><div>Lena Velumaro</div><div class="email">lena.velumaro@postfach.de</div></div>
    </div>
    <div class="badge">3</div>
  </aside>

  <main class="frame">
    <div class="topbar">
      <div class="edit-label">BEARBEITEN</div>
      <div class="page-info"><div>Home</div><div class="state">Seite · Veröffentlicht</div></div>
      <div class="device-toggle">
        <span class="on"><svg width="13" height="11" viewBox="0 0 13 11"><rect x="1" y="1" width="11" height="7" fill="none" stroke="#1a1a1a" stroke-width="1.3"/><line x1="4" y1="10" x2="9" y2="10" stroke="#1a1a1a" stroke-width="1.3"/></svg></span>
        <span><svg width="8" height="13" viewBox="0 0 8 13"><rect x="1" y="1" width="6" height="11" rx="1" fill="none" stroke="#555" stroke-width="1.2"/></svg></span>
      </div>
      <svg class="open-icon" width="11" height="11" viewBox="0 0 11 11"><path d="M1 10 L10 1 M4 1 H10 V7" fill="none" stroke="#1a1a1a" stroke-width="1.3"/></svg>
    </div>

    <header class="site-header">
      <div class="site-logo"><span class="dot"></span><span class="name">HOLMBERG</span></div>
      <nav class="site-nav">
        <a href="#">Coaching</a><a href="#">Training</a><a href="#">Ausbildungen</a><a href="#">Unternehmen</a><a href="#">Methoden</a>
        <span class="profile" aria-label="Profil"></span>
        <svg width="11" height="8" viewBox="0 0 11 8" aria-label="E-Mail"><rect x=".7" y=".7" width="9.6" height="6.6" fill="none" stroke="#1a1a1a" stroke-width="1.2"/><path d="M.7 .7 L5.5 4.5 L10.3 .7" fill="none" stroke="#1a1a1a" stroke-width="1.2"/></svg>
      </nav>
    </header>

    <section class="hero" role="img" aria-label="Foto einer Frau mit geschlossenen Augen im warmen Abendlicht">
      <ul class="hero-links">
        <li><a href="#">Coaching</a></li>
        <li><a href="#">Training</a></li>
        <li><a href="#">Blog</a></li>
        <li><a href="#">Methoden</a></li>
      </ul>
    </section>

    <section class="intro">Das ist in ein Blindtext. Hier erhalten Sie einen Überblick zu meinen</section>
    <div class="notice">AUF DIESER SEITE WERDEN VORSCHAUBILDER VON BILDARCHIV NORD VERWENDET. BITTE ERWERBE EINE BILDLIZENZ, UM DAS WASSERZEICHEN ZU ENTFERNEN.</div>
    <div class="help">?</div>
  </main>

  <div class="trial"><span>Deine Probephase endet in 14 Tagen. Jetzt upgraden, um deine Website optimal zu nutzen.</span><span class="cta">ABONNIEREN</span></div>
</div>
</body>
</html>
```